Veltrix Hand Sanitiser Spray Product Range for International Markets

Veltrix is a new Healthcare business launching a full product range of Anti-bacterial Hand Sanitiser Spray bottles in various sizes. We have a new logo which we believe differentiates us from the competition: Veltrix - Care That Stays With You
The Product Range will comprise two distinct product solution types:
- Anti-bacterial Hand Sanitisers - Alcohol based
- Anti-bacterial Hand Sanitisers - Sensitive Non Alcohol based
Bottle sizes will comprise a range containing:
100ml, 250ml, 500ml, 1ltr, 5ltr, 10ltr
Some bottles will have Pump Sprays
The Product labelling will be attractive front packaging label combined with strong product attributes and usage indicator cues.
As a Healthcare brand our logo design is light Green. We believe that this should be combined with blues and greens balanced to create contrast and strong stand-out on-shelf.
A review of competitor brands will show some similar colour cues, however as a Healthcare brand, the colour cues Green and White are synonymous with the sector. Many existing brands are very pragmatic in their label design. i.e. #it does what is says on the tin approach#. Our brand will need strong stand-out and strong aesthetic appeal too, since it will often be left in public view and around the home and office and therefore should look as attractive as possible. There will be other brand variants in the future and thought should be given to this too - with use of colour cues.
For Competitor indicators check-out the brands on Shopvale - Birch Lane, Dermalux and others....Thank-you!

Target Market(s)

First: Female 25 - 65
Second: Male 25 - 65

Contact Information for Business Card

Greg T. Hollis
CEO
Veltrix Healthcare International
'Care That Stays With You'
www.VeltrixHealthcare.example
E. gthollis@veltrixhealthcare.example
T. +44 7700 900312
T. +44 118 496051

Font styles to use
Sans Serif

Colors
34a7d7
33b8a4
add136
fbee3e
b768aa

```html
<!DOCTYPE html>
<html lang="en">
<head>
<meta charset="utf-8">
<title>Veltrix Hand Sanitiser Spray – Front Label</title>
<link rel="stylesheet" href="https://fonts.googleapis.com/css2?family=Marcellus&family=Montserrat:wght@500&family=Oswald:wght@400;500;700&family=Courgette&display=swap">
<style>
  :root {
    --page-bg: #f1f2f4;
    --label-bg: #ffffff;
    --ink-dark: #2f2f31;
    --ink-logo: #58585b;
    --ink-tagline: #5c5c60;
    --brand-blue: #34a7d7;
    --brand-teal: #33b8a4;
    --brand-lime: #add136;
    --splash-light: #e6f4f7;
    --splash-mid: #9fd4e6;
    --splash-teal: #a8e0d6;
  }
  * { margin: 0; padding: 0; box-sizing: border-box; }
  html, body {
    width: 800px; height: 1200px; overflow: hidden;
    background: var(--page-bg);
  }
  .canvas { position: relative; width: 800px; height: 1200px; }
  .label {
    position: absolute; left: 118px; top: 80px;
    width: 565px; height: 1040px;
    background: var(--label-bg);
    box-shadow: 0 10px 30px rgba(0,0,0,0.06);
    overflow: hidden;
  }
  .splash { position: absolute; left: 0; width: 100%; }
  .splash--top {
    top: 0; height: 330px;
    background:
      radial-gradient(ellipse at 25% 18%, var(--splash-mid) 0%, rgba(159,212,230,0) 55%),
      radial-gradient(ellipse at 70% 30%, var(--splash-teal) 0%, rgba(168,224,214,0) 50%),
      linear-gradient(180deg, var(--splash-light) 0%, rgba(255,255,255,0) 100%);
  }
  .splash--bottom {
    bottom: 0; height: 160px;
    background:
      radial-gradient(ellipse at 40% 100%, var(--splash-mid) 0%, rgba(159,212,230,0) 60%),
      radial-gradient(ellipse at 75% 100%, var(--splash-teal) 0%, rgba(168,224,214,0) 55%);
  }
  .brand {
    position: absolute; top: 360px; left: 0; width: 100%;
    text-align: center;
  }
  .brand__name {
    font-family: 'Marcellus', serif;
    font-size: 96px; line-height: 1;
    color: var(--ink-logo);
    letter-spacing: 1px;
  }
  .brand__tagline {
    margin-top: 8px;
    font-family: 'Montserrat', sans-serif;
    font-weight: 500; font-size: 15px;
    letter-spacing: 3px;
    color: var(--ink-tagline);
  }
  .product-name {
    position: absolute; top: 588px; left: 0; width: 100%;
    text-align: center;
    font-family: 'Oswald', sans-serif; font-weight: 700;
    font-size: 78px; line-height: 1;
    color: var(--ink-dark);
    letter-spacing: 1px;
  }
  .product-type {
    position: absolute; top: 664px; right: 48px;
    font-family: 'Courgette', cursive;
    font-size: 60px; line-height: 1;
    color: var(--brand-teal);
  }
  .badge {
    position: absolute; width: 94px; height: 94px;
    border-radius: 50%;
    display: flex; align-items: center; justify-content: center;
  }
  .badge svg { width: 54px; height: 54px; }
  .badge--skin { left: 68px; top: 760px; background: var(--brand-blue); }
  .badge--clean { left: 188px; top: 760px; background: var(--brand-teal); }
  .claim { position: absolute; left: 333px; top: 772px; width: 162px; text-align: center; }
  .claim__pill {
    height: 42px; border-radius: 8px;
    background: var(--brand-lime);
    font-family: 'Oswald', sans-serif; font-weight: 500;
    font-size: 20px; line-height: 42px; color: var(--ink-dark);
  }
  .claim__note {
    margin-top: 12px;
    font-family: 'Oswald', sans-serif; font-weight: 500;
    font-size: 18px; color: var(--ink-dark);
  }
</style>
</head>
<body>
<main class="canvas">
  <section class="label">
    <div class="splash splash--top" role="img" aria-label="Photograph of a clear water splash"></div>

    <div class="brand">
      <div class="brand__name">Veltrix</div>
      <div class="brand__tagline">CARE THAT STAYS WITH YOU</div>
    </div>

    <h1 class="product-name">HAND SANITIZER</h1>
    <div class="product-type">spray</div>

    <div class="badge badge--skin" aria-label="Gentle on skin">
      <svg viewBox="0 0 54 54" fill="none" stroke="#ffffff" stroke-width="3" stroke-linejoin="round">
        <path d="M27 6 C27 6 12 24 12 34 A15 15 0 0 0 42 34 C42 24 27 6 27 6 Z"/>
        <path d="M20 34 A7 7 0 0 0 27 41" stroke-linecap="round"/>
      </svg>
    </div>
    <div class="badge badge--clean" aria-label="Clean and fresh">
      <svg viewBox="0 0 54 54" fill="#ffffff">
        <path d="M22 8 L25 20 L37 23 L25 26 L22 38 L19 26 L7 23 L19 20 Z"/>
        <path d="M39 30 L41 37 L48 39 L41 41 L39 48 L37 41 L30 39 L37 37 Z"/>
      </svg>
    </div>

    <div class="claim">
      <div class="claim__pill">ANTI BACTERIAL</div>
      <div class="claim__note">Kills 99.99% Germs</div>
    </div>

    <div class="splash splash--bottom" role="img" aria-label="Photograph of water droplets splashing"></div>
  </section>
</main>
</body>
</html>
```